Kestrel Roofing & Restoration Business Card Design

Lookiing for a double sided business card design that will have rounded corners, will look good with Spot UV, Soft Laminate, or Gloss
Front of card should have Logo, Name and Contact Info, License numbers
Back of card should have Logo, maybe other small details

```html
<!DOCTYPE html>
<html lang="en">
<head>
<meta charset="utf-8">
<title>Kestrel Roofing &amp; Restoration – Business Cards</title>
<link href="https://fonts.googleapis.com/css2?family=Poppins:wght@400;500;600&display=swap" rel="stylesheet">
<style>
  :root {
    --stage: #141414;
    --card: #232323;
    --card-back: #1c1c1c;
    --white: #ffffff;
    --blue: #1aa3e8;
    --silver: #bdbdbd;
  }
  * { margin: 0; padding: 0; box-sizing: border-box; }
  html, body { width: 1200px; height: 875px; overflow: hidden; }
  body {
    background: var(--stage);
    font-family: "Poppins", sans-serif;
    color: var(--white);
    display: flex;
    align-items: center;
    justify-content: center;
    gap: 40px;
  }
  .card {
    width: 540px;
    height: 308px;
    border-radius: 22px;
    overflow: hidden;
    position: relative;
    box-shadow: 0 20px 50px rgba(0,0,0,.55);
  }

  /* Back */
  .card--back { background: var(--card-back); }
  .back-pattern {
    position: absolute; inset: 0;
    background: linear-gradient(100deg, #d9d9d9 0%, #8a8a8a 22%, #3a3a3a 45%, #161616 70%, #0e0e0e 100%);
    opacity: .55;
  }
  .back-name {
    position: absolute;
    right: 70px; top: 150px;
    font-size: 30px; font-weight: 600;
    color: var(--white);
    display: flex; align-items: center; gap: 10px;
  }
  .back-name .mark { width: 14px; height: 14px; background: var(--blue); border-radius: 50%; }

  /* Front */
  .card--front {
    background: var(--card);
    display: flex;
    align-items: center;
    padding: 0 34px 0 40px;
  }
  .brand {
    width: 250px;
    font-size: 22px;
    font-weight: 500;
    line-height: 1.25;
    text-transform: uppercase;
    letter-spacing: .5px;
    color: var(--white);
  }
  .divider {
    width: 2px; height: 200px;
    background: var(--blue);
    margin: 0 30px 0 14px;
  }
  .contact { font-size: 11.5px; line-height: 1.45; }
  .contact__name { color: var(--blue); font-size: 21px; font-weight: 600; line-height: 1.1; }
  .contact__role { font-size: 12px; margin-bottom: 6px; }
  .contact__license { margin-bottom: 12px; }
  .contact__license span { color: var(--blue); }
  .contact__list { list-style: none; margin-bottom: 12px; }
  .contact__list li { display: flex; align-items: center; gap: 8px; }
  .contact__list svg { width: 11px; height: 11px; fill: var(--blue); flex: none; }
</style>
</head>
<body>

  <section class="card card--back" aria-label="Card back">
    <div class="back-pattern" role="img" aria-label="Repeating brand pattern in spot UV, fading from silver to black"></div>
    <div class="back-name"><span class="mark"></span>Kestrel</div>
  </section>

  <section class="card card--front" aria-label="Card front">
    <div class="brand">Kestrel<br>Roofing &amp;<br>Restoration</div>
    <div class="divider"></div>
    <div class="contact">
      <p class="contact__name">Daniel Hartley</p>
      <p class="contact__role">Head contractor</p>
      <p class="contact__license"><span>License</span> #40817</p>
      <ul class="contact__list">
        <li><svg viewBox="0 0 24 24"><path d="M6.6 10.8a15 15 0 0 0 6.6 6.6l2.2-2.2a1 1 0 0 1 1-.25 11.4 11.4 0 0 0 3.6.57 1 1 0 0 1 1 1V20a1 1 0 0 1-1 1A17 17 0 0 1 3 4a1 1 0 0 1 1-1h3.5a1 1 0 0 1 1 1c0 1.25.2 2.45.57 3.57a1 1 0 0 1-.25 1z"/></svg>+44 7700 900418</li>
        <li><svg viewBox="0 0 24 24"><path d="M7 1h10a2 2 0 0 1 2 2v18a2 2 0 0 1-2 2H7a2 2 0 0 1-2-2V3a2 2 0 0 1 2-2zm0 3v14h10V4zm5 15.5a1 1 0 1 0 0 2 1 1 0 0 0 0-2z"/></svg>+44 7700 900418</li>
        <li><svg viewBox="0 0 24 24"><path d="M2 5h20v14H2zm2 2v.5l8 5 8-5V7z"/></svg>name@kestrelroofing.co.uk</li>
        <li><svg viewBox="0 0 24 24"><path d="M12 2a10 10 0 1 0 0 20 10 10 0 0 0 0-20zm-1 17.9A8 8 0 0 1 4.1 11H7c.1 3 1.4 6.4 4 8.9zM7 9H4.1A8 8 0 0 1 11 4.1C8.4 6.6 7.1 9 7 9zm6 10.9c2.6-2.5 3.9-5.9 4-8.9h2.9a8 8 0 0 1-6.9 8.9zM17 9c-.1 0-1.4-2.4-4-4.9A8 8 0 0 1 19.9 9z"/></svg>www.kestrelroofing.co.uk</li>
      </ul>
      <p class="contact__address">42 Harbour View Lane<br>Millbrook, NJ 07000 USA</p>
    </div>
  </section>

</body>
</html>
```